VerdaLifeRX supplement bottle design

We need to redesign our artwork for our line of supplements that is fresh and informative. There are certain design parameters that must be followed for size and content. I will attached our latest design. We want to change our fat metabolizer to fat burner and Gi Stabilizer to Colon Cleanse. The Gi Stabilizer file was too large to upload. The rest stay the same. Here is a link to website www.verdaliferx.example.

Industry/Entity Type

Health And Wellness

Requirements
Must have
• All disclaimers and who it is produced for
Nice to have
• Fresh look and proper information

```html
<!DOCTYPE html>
<html lang="en">
<head>
<meta charset="utf-8">
<title>VerdaLifeRX Multi-Vitamin Label</title>
<link rel="stylesheet" href="https://fonts.googleapis.com/css2?family=Comfortaa:wght@400;600&family=Tinos:wght@400;700&display=swap">
<style>
  :root {
    --page: #ffffff;
    --navy: #16305f;
    --blue: #2b64a6;
    --blue-light: #3f7fc0;
    --purple: #7b3fa2;
    --purple-line: #8d4bb5;
    --white: #ffffff;
    --ink: #111111;
  }
  html, body {
    margin: 0;
    padding: 0;
    width: 963px;
    height: 1200px;
    overflow: hidden;
    background: var(--page);
  }
  .canvas {
    position: relative;
    width: 963px;
    height: 1200px;
  }
  .label {
    position: absolute;
    left: 31px;
    top: 413px;
    width: 1050px;
    height: 437px;
    transform: scale(0.857);
    transform-origin: 0 0;
    background: radial-gradient(ellipse at 45% 35%, var(--blue-light) 0%, var(--blue) 40%, var(--navy) 100%);
    color: var(--white);
    font-family: "Comfortaa", sans-serif;
    overflow: hidden;
  }
  .usage {
    position: absolute;
    left: 27px;
    top: 14px;
    width: 235px;
    font-size: 12.5px;
    line-height: 17.5px;
  }
  .usage h3 {
    font-family: "Tinos", serif;
    font-weight: 400;
    font-size: 13.5px;
    margin: 0;
    letter-spacing: 0.3px;
  }
  .usage p { margin: 0 0 16px; }
  .disclaimer {
    border: 1px solid var(--white);
    padding: 3px 5px;
    margin-top: -2px;
  }
  .brand {
    position: absolute;
    left: 355px;
    top: 45px;
    font-size: 38px;
    font-weight: 400;
    color: var(--purple);
    letter-spacing: -0.5px;
  }
  .brand-rule {
    position: absolute;
    left: 355px;
    top: 97px;
    width: 240px;
    height: 3px;
    background: var(--purple-line);
  }
  .product-name {
    position: absolute;
    left: 445px;
    top: 115px;
    width: 250px;
    height: 40px;
    background: var(--purple);
    font-size: 33px;
    line-height: 40px;
    text-align: center;
    letter-spacing: -1px;
  }
  .descriptor {
    position: absolute;
    left: 352px;
    top: 185px;
    font-size: 25px;
    line-height: 36px;
  }
  .descriptor .line-1 {
    display: block;
    border-bottom: 2px solid var(--purple-line);
    width: 255px;
  }
  .descriptor-rule {
    position: absolute;
    left: 352px;
    top: 262px;
    width: 270px;
    height: 2px;
    background: var(--purple-line);
  }
  .features {
    position: absolute;
    left: 352px;
    top: 292px;
    margin: 0;
    padding: 0;
    list-style: none;
    font-size: 19px;
    line-height: 30px;
  }
  .features li::before {
    content: "";
    display: inline-block;
    width: 7px;
    height: 7px;
    border-radius: 50%;
    background: var(--purple-line);
    margin-right: 12px;
    vertical-align: middle;
  }
  .count {
    position: absolute;
    left: 618px;
    top: 258px;
    width: 95px;
    height: 86px;
    background: var(--purple);
    border-radius: 4px;
    text-align: center;
  }
  .count .number { display: block; font-size: 50px; line-height: 58px; }
  .count .unit { display: block; font-size: 19px; line-height: 18px; }
  .facts {
    position: absolute;
    left: 790px;
    top: 20px;
    width: 241px;
    background: var(--white);
    color: var(--ink);
    border: 1px solid var(--ink);
    padding: 3px 6px 6px 8px;
    box-sizing: border-box;
    font-size: 11.5px;
    line-height: 19px;
  }
  .facts h2 {
    font-family: "Tinos", serif;
    font-weight: 700;
    font-size: 25px;
    line-height: 28px;
    margin: 0;
    border-bottom: 2px solid var(--ink);
  }
  .facts .row { border-bottom: 1px solid var(--ink); display: flex; justify-content: space-between; white-space: nowrap; }
  .facts .row.plain { border-bottom: none; }
  .facts .thick { border-bottom: 2px solid var(--ink); }
  .facts .value { font-size: 8px; }
  .other {
    position: absolute;
    left: 790px;
    top: 168px;
    width: 240px;
    font-size: 12.5px;
    line-height: 17.5px;
  }
  .other h3 {
    font-family: "Tinos", serif;
    font-weight: 700;
    font-size: 13.5px;
    margin: 0;
  }
  .other p { margin: 0; }
  .warning {
    position: absolute;
    left: 790px;
    top: 313px;
    width: 240px;
    font-size: 12px;
    line-height: 17.5px;
    margin: 0;
  }
  .base-rule {
    position: absolute;
    left: 0;
    top: 405px;
    width: 100%;
    height: 3px;
    background: var(--purple-line);
  }
</style>
</head>
<body>
<div class="canvas">
  <section class="label">
    <div class="usage">
      <h3>SUGGESTED USE:</h3>
      <p>1 tablet taken 1 to 4 times daily preferably with a meal or as directed by a healthcare professional</p>
      <h3>CAUTION:</h3>
      <p>Do not exceed recommended dose. pregnant or nursing mothers, children under 18, and individuals with a know medical condition any dietry supplement. This product is manufactured and packaged in facility which may also process milk, soy, wheat, egg, peanuts, tree nuts, fish and crustacean shellfish.</p>
      <p class="disclaimer">These statements have not beeen evaluated by the food and drug administration. This product is not intended to diagnose, treat, cure, or prevent any disease.</p>
    </div>

    <div class="brand">VerdaLifeRX</div>
    <div class="brand-rule"></div>
    <div class="product-name">MULTI-VITAMIN</div>

    <div class="descriptor">
      <span class="line-1">Food Based Vitamin</span>
      <span>Mineral Complex</span>
    </div>
    <div class="descriptor-rule"></div>

    <ul class="features">
      <li>Non-GMO Formula</li>
      <li>Dietary Supplement</li>
    </ul>

    <div class="count">
      <span class="number">30</span>
      <span class="unit">Tablets</span>
    </div>

    <div class="facts">
      <h2>Supplement Facts</h2>
      <div class="row plain">Serving Size 1 tablet</div>
      <div class="row thick">Serving Per Container: 60</div>
      <div class="row">Amount Per Serving / Daily Value</div>
      <div class="row">Vitamin D-3 (cholecalciferol)<span class="value">250 IU 63%</span></div>
      <div class="row plain">Calcium (Carbonate)<span class="value">250mg 25%</span></div>
    </div>

    <div class="other">
      <h3>Other Ingredients:</h3>
      <p>Microcrystalline cellulose, acid aqueous clear film coat (HPMC, PEG and purified water), vegetable magnesium stearate and silicon dioxide.</p>
    </div>

    <p class="warning">KEEP OUT OF THE REACH OF CHILDREN. DO NOT USE IF SAFETY SEAL IS DAMAGED OR MISSING. STORE IN COOL, DRY PLACE.</p>

    <div class="base-rule"></div>
  </section>
</div>
</body>
</html>
```